Business Card Design for a Lending Business (Hard Money loans)

We need a business card for our Real Estate Lending business. We do hard Money loans for real estate investors. We have an existing logo we like, see attached. I'd like the business card to mostly include the logo colors, but a bright color pop of some sort would be nice to see also. Card should include Logo, Company Name, Company Address, Employee Name, Cell Phone, Main Phone, Email, Website

Industry/Entity Type

Finance / Lending

Contact Information for Business Card

Logo, Company Name, Company Address, Employee Name, Cell Phone, Main Phone, Email, Website

Requirements
Nice to have
• I'd like the business card to mostly include the logo colors, but a bright color pop of some sort would be nice to see also.

```html
<!DOCTYPE html>
<html lang="en">
<head>
<meta charset="utf-8">
<title>Harborline Lending – Business Card</title>
<link rel="stylesheet" href="https://fonts.googleapis.com/css2?family=Montserrat:wght@400;500;700;800&display=swap">
<style>
  :root {
    --navy: #1f2a86;
    --navy-deep: #27318f;
    --sky: #1fa3dc;
    --ink: #3c3c44;
    --paper: #ffffff;
    --backdrop: #8a8a88;
  }
  * { margin: 0; padding: 0; box-sizing: border-box; }
  html, body { width: 1200px; height: 801px; overflow: hidden; }
  body {
    background: var(--backdrop);
    font-family: "Montserrat", Arial, sans-serif;
    position: relative;
  }
  .card {
    position: absolute;
    top: 246px;
    width: 540px;
    height: 309px;
    border-radius: 2px;
    overflow: hidden;
  }
  .card--front { left: 40px; background: var(--paper); }
  .card--back { left: 620px; background: var(--navy-deep); }

  /* front */
  .brand {
    position: absolute;
    left: 16px;
    width: 230px;
    top: 100px;
    display: flex;
    flex-direction: column;
    align-items: center;
    gap: 14px;
  }
  .brand__dot {
    width: 44px; height: 44px;
    border-radius: 50%;
    background: var(--sky);
  }
  .brand__name {
    color: var(--navy);
    font-weight: 700;
    font-size: 19px;
    letter-spacing: 0.5px;
    white-space: nowrap;
  }
  .divider {
    position: absolute;
    left: 262px;
    top: 64px;
    width: 1.5px;
    height: 182px;
    background: var(--navy);
  }
  .contact {
    position: absolute;
    left: 284px;
    top: 60px;
    color: var(--ink);
  }
  .contact__name {
    color: var(--navy);
    font-weight: 800;
    font-size: 17px;
    letter-spacing: 0.3px;
  }
  .contact__title {
    color: var(--sky);
    font-weight: 500;
    font-size: 12px;
    margin-top: 2px;
  }
  .contact__address {
    font-size: 11.5px;
    line-height: 1.5;
    margin-top: 12px;
  }
  .contact__list {
    list-style: none;
    margin-top: 12px;
    font-size: 11.5px;
    line-height: 1.55;
  }
  .contact__list li { display: flex; align-items: center; gap: 7px; }
  .contact__list svg { width: 10px; height: 10px; flex: none; }

  /* back */
  .back__pattern {
    position: absolute;
    inset: 0;
    background: linear-gradient(135deg, #1d2678 0%, #2a3494 55%, #4853a8 100%);
  }
  .back__brand {
    position: absolute;
    right: 48px;
    top: 122px;
    display: flex;
    align-items: center;
    gap: 8px;
    color: var(--paper);
    font-weight: 700;
    font-size: 15px;
  }
  .back__brand .brand__dot { width: 20px; height: 20px; background: var(--paper); }
</style>
</head>
<body>

<section class="card card--front" aria-label="Card front">
  <div class="brand">
    <span class="brand__dot"></span>
    <span class="brand__name">Harborline Lending</span>
  </div>

  <div class="divider"></div>

  <div class="contact">
    <p class="contact__name">MARK TOLLIVER</p>
    <p class="contact__title">President</p>
    <p class="contact__address">1250 Meadow Ridge Rd.<br>Fallston MD 21047</p>
    <ul class="contact__list">
      <li>
        <svg viewBox="0 0 10 10"><rect x="2.5" y="0.5" width="5" height="9" rx="1" fill="none" stroke="#1fa3dc" stroke-width="1"/></svg>
        410-555-0142
      </li>
      <li>
        <svg viewBox="0 0 10 10"><path d="M2 1 L4 3 L3 4.5 Q4.5 6.5 5.5 7 L7 6 L9 8 L7.5 9.5 Q2.5 8 0.5 2.5 Z" fill="#1fa3dc"/></svg>
        410-555-0142
      </li>
      <li>
        <svg viewBox="0 0 10 10"><rect x="0.5" y="2" width="9" height="6.5" fill="#1fa3dc"/><path d="M0.5 2 L5 6 L9.5 2" fill="none" stroke="#fff" stroke-width="0.8"/></svg>
        info@HarborlineLending.com
      </li>
      <li>
        <svg viewBox="0 0 10 10"><circle cx="5" cy="5" r="4.5" fill="#1fa3dc"/><path d="M0.5 5 H9.5 M5 0.5 Q2.5 5 5 9.5 M5 0.5 Q7.5 5 5 9.5" fill="none" stroke="#fff" stroke-width="0.7"/></svg>
        www.HarborlineLending.com
      </li>
    </ul>
  </div>
</section>

<section class="card card--back" aria-label="Card back">
  <div class="back__pattern" role="img" aria-label="Repeating embossed monogram pattern in navy tones across the card back"></div>
  <div class="back__brand">
    <span class="brand__dot"></span>
    <span>Harborline Lending</span>
  </div>
</section>

</body>
</html>
```